NOTE: I PROVIDED THE INCORRECT LOGO AND ONLY A HANDFUL OF PEOPLE NOTICED THAT IT WAS NOT THE ONE I DESCRIBED. THE LOGO I HAVE NOW ATTACHED MATCHES MY WEBSITE AND THE COLORS ON THE WEBSITE SHOULD BE USED FOR THE CARD.

PLEASE READ THE BUSINESS CARD DETAILS AND PROJECT MUST HAVES CAREFULLY.

I am looking for a business card that is powerful, a bit edgy, and although I work in the corporate world, not too formal. I would like to see designs that use the colors on my website www.brightmoorlane.com. I don't want the card to look washed out so please use shades of those colors that make them "pop". The "vibe" of the card needs to show substance and confidence while also reflecting that we're not your usual consultants.

The focus of my work is turning "people problems" into profits. Those problems could be poor service, an unstable workforce, untrained leaders, or managing change. We are an aggressive, results-focused team of performance improvement professionals who refuse to believe "things can't be done". For us, failure is not an option. Our logo reflects a target from the view of the site on a gun.

In addition to the contact information provided on the sample business card (do not include "turning people problems into profits"), I would like to include this statement (probably on the back):
I equip results-oriented business leaders to turn their people problems into profits in six months or less.

PLEASE NOTE THAT MY WEBSITE IS UNDER REVISION TO TONE DOWN THE MILITARY THEME, ALTHOUGH THE WARRIOR ENERGY AND FOCUS ON RESULTS REMAINS.

Target Market(s)

My clients are Mid and senior-level managers. I don't target any particular industry.

Industry/Entity Type

Consulting

Contact Information for Business Card

In addition to the contact information provided on the sample business card (DO NOT INCLUDE "turning people problems into profits"), I would like to include this statement (probably on the back):

I don't care whether the card is landscape or portrait view.

Font styles to use
Sans Serif

Requirements
Must have
• 1. be easy to read, no 6-8 point fonts!
• 2. a "vibe" that captures the eye without being too chaotic or busy
• 3. bold color, not washed out or boring - a good blend with the colors currently on my website (black, red, white, army green) but you don't need to use all of them.
• 4. all the contact information I have provided
• 5. a good blend with the colors currently on my website
• 6. Must have this quote on the back of the card: I equip results-oriented business leaders to turn their people problems into profits in six months or less.
Nice to have
• In looking at the sample images I provided for ideas, you can see that I like the way a card carries over from one side to the next.
• It would be great to find some aspect/quality/feature that I haven't seen before
Should not have
• 1. NO use of ALL CAPS
• 2. fonts that I would have to seek out and purchase (you should provide files for font if using something not standard)

```html
<!DOCTYPE html>
<html lang="en">
<head>
<meta charset="utf-8">
<title>Brightmoor Lane – Business Card</title>
<link href="https://fonts.googleapis.com/css2?family=Open+Sans:wght@400;700&display=swap" rel="stylesheet">
<style>
  :root {
    --backdrop: #2b2b2d;
    --card-white: #ffffff;
    --army-green: #3f4530;
    --army-green-soft: #4a5139;
    --signal-red: #ee3b33;
    --ink: #333333;
    --brand-ink: #34382a;
    --quote-ink: #e6e8df;
  }
  * { box-sizing: border-box; margin: 0; padding: 0; }
  html, body {
    width: 1200px; height: 782px; overflow: hidden;
    background: var(--backdrop);
    font-family: "Open Sans", Arial, sans-serif;
  }
  .stage {
    position: relative; width: 1200px; height: 782px;
    display: flex; align-items: center; justify-content: center; gap: 40px;
  }
  .card {
    position: relative; width: 540px; height: 309px; overflow: hidden;
  }

  /* Front */
  .card--front { background: var(--card-white); }
  .card__bands { position: absolute; inset: 0; width: 100%; height: 100%; }
  .holder { position: absolute; left: 34px; top: 44px; }
  .holder__name {
    font-size: 16px; font-weight: 700; color: var(--brand-ink); letter-spacing: 0.2px;
  }
  .holder__title { font-size: 14px; color: var(--signal-red); margin-top: 1px; }

  .phones { position: absolute; left: 34px; top: 150px; list-style: none; }
  .phones li, .online li {
    display: flex; align-items: center; gap: 7px;
    font-size: 14.5px; color: var(--ink); line-height: 1.3;
  }
  .icon { width: 11px; height: 11px; fill: var(--ink); flex: none; }

  .brand {
    position: absolute; left: 262px; top: 152px;
    display: flex; align-items: center; gap: 10px;
  }
  .brand__dot {
    width: 22px; height: 22px; border-radius: 50%; background: var(--signal-red); flex: none;
  }
  .brand__name {
    font-size: 26px; font-weight: 700; color: var(--brand-ink); letter-spacing: -0.3px;
    white-space: nowrap;
  }

  .online {
    position: absolute; right: 40px; top: 212px; list-style: none; text-align: right;
  }
  .online li { justify-content: flex-end; font-size: 15px; }

  /* Back */
  .card--back { background: var(--army-green); }
  .back__pattern {
    position: absolute; inset: 0;
    background: radial-gradient(circle at 50% 45%, var(--army-green-soft), var(--army-green) 75%);
  }
  .back__brand {
    position: absolute; left: 290px; top: 118px;
    display: flex; align-items: center; gap: 9px;
  }
  .back__dot { width: 20px; height: 20px; border-radius: 50%; background: var(--signal-red); flex: none; }
  .back__name { font-size: 22px; font-weight: 700; color: var(--card-white); white-space: nowrap; }
  .back__quote {
    position: absolute; left: 34px; right: 34px; bottom: 30px;
    font-size: 14px; line-height: 1.45; color: var(--quote-ink);
  }
</style>
</head>
<body>
<main class="stage">
  <section class="card card--front" aria-label="Card front">
    <svg class="card__bands" viewBox="0 0 540 309" aria-hidden="true">
      <polygon points="0,262 240,262 222,309 0,309" fill="var(--army-green)"/>
      <polygon points="250,282 540,282 540,309 232,309" fill="var(--signal-red)"/>
    </svg>

    <div class="holder">
      <p class="holder__name">Dana Whitfield</p>
      <p class="holder__title">Chief Performance Strategist</p>
    </div>

    <ul class="phones">
      <li>
        <svg class="icon" viewBox="0 0 12 12"><path d="M1 3c0-1 1-2 2-2h6c1 0 2 1 2 2v1H8V3H4v1H1z M2 5h8l1 6H1z"/></svg>
        555-214-7780
      </li>
      <li>
        <svg class="icon" viewBox="0 0 12 12"><path d="M3 0h6v12H3z M4 1v8h4V1z"/></svg>
        555-309-4126
      </li>
    </ul>

    <div class="brand">
      <span class="brand__dot"></span>
      <span class="brand__name">Brightmoor Lane</span>
    </div>

    <ul class="online">
      <li>dana@brightmoorlane.com
        <svg class="icon" viewBox="0 0 12 12"><path d="M0 2h12v8H0z M1 3l5 4 5-4z" fill-rule="evenodd"/></svg>
      </li>
      <li>www.brightmoorlane.com
        <svg class="icon" viewBox="0 0 12 12"><circle cx="6" cy="6" r="6"/></svg>
      </li>
    </ul>
  </section>

  <section class="card card--back" aria-label="Card back">
    <div class="back__pattern" role="img" aria-label="Faint repeating brand mark pattern across the green background"></div>
    <div class="back__brand">
      <span class="back__dot"></span>
      <span class="back__name">Brightmoor Lane</span>
    </div>
    <p class="back__quote">I equip results-oriented business leaders to turn their people problems into profits in six months or less.</p>
  </section>
</main>
</body>
</html>
```